A guide to healing depression needs a great cover

An experienced therapist and former patient have put together a great guide to help people living with depression and their loved ones.
With the extraordinary combination of real case studies, checklists, clearly formulated medical content, helpful and detailed steps and practical exercises, everyone can learn how to put their own life back on the right track. We put an end to the constant worries, rebuild your self-esteem and start with positive thoughts into a happy future.
We imagine the sufferer coming out of the darkness and walking into the sunrise (or something like that). A very bright cover, which symbolizes light, would also be possible. Attached you will find an image that appealed to us, but which seems too cheap.

Target Market(s)

Depressed people and their families

Font styles to use
Serif

Requirements
Must have
• go from darkness into light
Nice to have
• For the title, it would be great if the word depression were highlighted
Should not have
• don't look cheap

```html
<!DOCTYPE html>
<html lang="de">
<head>
<meta charset="utf-8">
<title>Liebe Schwermut, es ist genug!</title>
<link rel="stylesheet" href="https://fonts.googleapis.com/css2?family=Cinzel:wght@400&family=Arimo:wght@400&display=swap">
<style>
  :root {
    --ink: #000000;
    --paper: #ffffff;
    --sky-top: #c80000;
    --sky-mid: #f05a0a;
    --sun-glow: #ffb000;
    --sun-core: #fff200;
  }
  html, body {
    margin: 0;
    padding: 0;
    overflow: hidden;
    background: var(--ink);
  }
  .cover {
    position: relative;
    width: 840px;
    height: 1200px;
    overflow: hidden;
    background: var(--ink);
    font-family: "Arimo", Arial, sans-serif;
    color: var(--paper);
  }
  .sunrise-art {
    position: absolute;
    left: 0;
    top: 0;
    width: 840px;
    height: 650px;
    background:
      radial-gradient(ellipse 520px 560px at 440px 600px,
        var(--sun-core) 0%,
        var(--sun-glow) 22%,
        var(--sky-mid) 52%,
        var(--sky-top) 100%);
  }
  .authors {
    position: absolute;
    left: 0;
    top: 72px;
    width: 840px;
    margin: 0;
    text-align: center;
    font-size: 34px;
    font-weight: 400;
    line-height: 1.2;
    color: var(--paper);
  }
  .title {
    position: absolute;
    left: 0;
    top: 0;
    width: 840px;
    height: 1200px;
    pointer-events: none;
  }
  .title text {
    font-family: "Cinzel", "Trajan Pro", serif;
    fill: var(--paper);
  }
  .subtitle {
    position: absolute;
    left: 0;
    top: 970px;
    width: 840px;
    margin: 0;
    text-align: center;
    font-size: 23px;
    line-height: 29.6px;
    color: var(--paper);
  }
</style>
</head>
<body>
  <main class="cover">
    <div class="sunrise-art" role="img" aria-label="Silhouette of a person with raised arms standing in grass before a radiant red-orange sunrise with light rays"></div>

    <p class="authors">Dipl.-Psych. Jonas Weidner &amp; Mark Holler</p>

    <svg class="title" viewBox="0 0 840 1200" aria-labelledby="cover-title">
      <title id="cover-title">Liebe Schwermut, es ist genug!</title>
      <text class="title-lead" x="420" y="728" font-size="54" text-anchor="middle" textLength="520" lengthAdjust="spacingAndGlyphs">LIEBE SCHWERMUT,</text>
      <text class="title-main" x="420" y="850" font-size="112" text-anchor="middle" textLength="660" lengthAdjust="spacingAndGlyphs">ES IST GENUG!</text>
    </svg>

    <p class="subtitle">
      Therapie-Tools für den Alltag: Mit konkreten<br>
      Übungen &amp; Beispielen eines erfahrenen Therapeuten<br>
      negative Gedanken und Depressionen überwinden<br>
      Für Betroffene &amp; Angehörige
    </p>
  </main>
</body>
</html>
```